Company PowerPoint Presentation Template

I am looking for a business powerpoint template tailored to my company that specializes in permafrost services for the mining, transportation, and oil & gas industries. The template would be used to present project findings from studies completed for our clients. I am looking for a crisp, technical, professional business look to the template. Our business is located in North America and English is the primary language used to communicate our work. Complimentary colors associated with the business is blue (RGB, 0,112,192) or something similar in color.

```html
<!DOCTYPE html>
<html lang="en">
<head>
<meta charset="utf-8">
<title>Talik Permafrost Consulting – Presentation Template</title>
<link href="https://fonts.googleapis.com/css2?family=Michroma&family=Roboto:wght@400;500;700&display=swap" rel="stylesheet">
<style>
:root{
  --navy:#141b26;
  --blue:#0a6fd0;
  --page:#eef3f9;
  --white:#ffffff;
  --ink:#1d2330;
  --muted:#5d6470;
}
*{box-sizing:border-box;margin:0;padding:0}
html,body{width:1200px;height:4739px;overflow:hidden}
body{background:var(--page);font-family:'Roboto',Arial,sans-serif;color:var(--ink);position:relative}
.slide{position:absolute;left:76px;width:1048px;height:589px;background:var(--white);overflow:hidden;box-shadow:0 6px 22px rgba(20,40,80,.12)}
.slide--content{border-bottom:5px solid var(--blue)}
.bg-svg{position:absolute;inset:0;width:100%;height:100%}
.brand{position:absolute;font-family:'Michroma',sans-serif;line-height:1}
.brand__name{font-size:26px;letter-spacing:2px;display:block}
.brand__sub{font-family:'Roboto',sans-serif;font-size:8.5px;letter-spacing:4px;display:block;margin-top:5px}
.brand--light{color:var(--white)}
.brand--dark{color:var(--navy);right:60px;top:30px;text-align:center}
.hero-title{position:absolute;left:60px;top:240px;color:var(--white)}
.hero-title h1{font-family:'Michroma',sans-serif;font-weight:400;font-size:38px;letter-spacing:1px}
.hero-title h2{font-family:'Roboto',sans-serif;font-weight:500;color:var(--blue);font-size:19px;letter-spacing:4.5px;margin-top:16px}
.hero-title p{font-size:16.5px;line-height:1.6;margin-top:14px;width:370px}
.head{position:absolute;left:0;top:0;width:700px;height:90px}
.head__title{position:absolute;left:60px;top:27px;color:var(--white);font-family:'Michroma',sans-serif;font-size:24px;letter-spacing:.5px}
.photo{position:absolute;border-radius:10px}
.bio{position:absolute;left:588px;top:224px;width:404px;font-size:12.6px;line-height:1.85;color:var(--muted);text-align:justify}
.bio p+p{margin-top:12px}
.pill{position:absolute;left:116px;top:138px;width:816px;height:230px;border-radius:115px;background:linear-gradient(90deg,#4b4a5c 0%,#b8603a 35%,#f6a040 50%,#b05535 66%,#3d4255 100%)}
.icon-disc{position:absolute;width:80px;height:80px;border-radius:50%;background:var(--blue);border:6px solid var(--white);box-shadow:0 4px 12px rgba(0,0,0,.2);display:flex;align-items:center;justify-content:center}
.col{position:absolute;width:330px;text-align:center}
.col h3,.card h3{font-size:13px;font-weight:700;color:var(--ink)}
.col p{font-size:12.3px;line-height:1.7;color:var(--muted);margin-top:14px}
.card{position:absolute;top:158px;width:276px;height:362px;border-radius:12px;background:var(--white);box-shadow:0 4px 18px rgba(0,0,0,.14);text-align:center;padding:6px}
.card__img{height:180px;border-radius:10px}
.card h3{margin-top:20px;line-height:1.55}
.card__rule{width:48px;height:3px;background:var(--blue);margin:6px auto 0}
.card p{font-size:11.5px;line-height:1.6;color:var(--muted);margin:14px 16px 0}
.project{position:absolute;top:176px;width:292px}
.project__img{height:215px}
.project__cap{position:relative;margin:-22px 12px 0;background:var(--white);box-shadow:0 4px 14px rgba(0,0,0,.14);height:110px;padding:22px 18px 0;text-align:center;font-size:13px;font-weight:700;line-height:1.65;text-transform:uppercase}
.thanks{position:absolute;left:60px;top:196px;color:var(--white)}
.thanks h1{font-family:'Michroma',sans-serif;font-weight:400;font-size:36px;letter-spacing:1px;white-space:nowrap}
.contact{list-style:none;margin-top:36px}
.contact li{display:flex;align-items:center;gap:22px;font-size:16px;height:45px}
.contact svg{width:30px;height:30px;flex:none}
</style>
</head>
<body>

<section class="slide" style="top:101px">
  <svg class="bg-svg" viewBox="0 0 1048 589" aria-hidden="true">
    <defs><linearGradient id="sea" x1="0" y1="0" x2="0" y2="1"><stop offset="0" stop-color="#bfc3c8"/><stop offset=".55" stop-color="#8d9298"/><stop offset="1" stop-color="#3a3f45"/></linearGradient></defs>
    <rect width="1048" height="589" fill="var(--navy)"/>
    <polygon points="360,0 372,0 633,589 621,589" fill="#fff"/>
  </svg>
  <svg class="bg-svg" viewBox="0 0 1048 589" role="img" aria-label="Offshore drilling platform at sea with a tanker, black and white">
    <polygon points="372,0 1048,0 1048,589 633,589" fill="url(#sea)"/>
    <polygon points="392,589 632,589 478,332" fill="var(--blue)"/>
  </svg>
  <div class="brand brand--light" style="left:60px;top:40px"><span class="brand__name">TALIK</span><span class="brand__sub">PERMAFROST CONSULTING</span></div>
  <div class="hero-title">
    <h1>TALIK</h1>
    <h2>PERMAFROST CONSULTING</h2>
    <p>We provide specialized permafrost services to the mining, transportation, and oil &amp; gas industries.</p>
  </div>
</section>

<section class="slide slide--content" style="top:759px">
  <svg class="head" viewBox="0 0 700 90" aria-hidden="true"><polygon points="0,0 690,0 645,82 0,82" fill="var(--navy)"/><polygon points="0,82 645,82 643,88 0,88" fill="var(--blue)"/><polygon points="654,82 698,0 700,0 657,86" fill="var(--blue)"/></svg>
  <div class="head__title">PRINCIPAL CONSULTANT</div>
  <div class="brand brand--dark"><span class="brand__name">TALIK</span><span class="brand__sub">PERMAFROST CONSULTING</span></div>
  <div class="photo" style="left:61px;top:166px;width:463px;height:342px;background:linear-gradient(180deg,#8a97a6 0%,#e9b273 55%,#6e5a4a 100%)" role="img" aria-label="Semi truck on a highway at sunset"></div>
  <div class="bio">
    <p>Daniel is a geocryologist with 18 years of experience working on Arctic and Subarctic projects. He specializes in permafrost and ground ice characterization, periglacial geomorphology, ground thermal analysis, numerical thermal modeling, thermal design of infrastructure, and development of permafrost mitigation measures to improve ground stability.</p>
    <p>Daniel has worked widely on both terrestrial and subsea permafrost related to mining, transportation, and oil and gas industries in the USA, Canada, Russia, and Greenland.</p>
  </div>
</section>

<section class="slide slide--content" style="top:1417px">
  <svg class="head" viewBox="0 0 700 90" aria-hidden="true"><polygon points="0,0 690,0 645,82 0,82" fill="var(--navy)"/><polygon points="0,82 645,82 643,88 0,88" fill="var(--blue)"/><polygon points="654,82 698,0 700,0 657,86" fill="var(--blue)"/></svg>
  <div class="head__title">OUR MISSION &amp; VISION</div>
  <div class="brand brand--dark"><span class="brand__name">TALIK</span><span class="brand__sub">PERMAFROST CONSULTING</span></div>
  <div class="pill" role="img" aria-label="Industrial pipelines leading to a refinery at sunset"></div>
  <div class="icon-disc" style="left:301px;top:322px"><svg width="36" height="36" viewBox="0 0 36 36" fill="none" stroke="#fff" stroke-width="2.4"><circle cx="17" cy="19" r="13"/><circle cx="17" cy="19" r="7"/><circle cx="17" cy="19" r="1.5" fill="#fff"/><path d="M17 19 30 6M25 6h5v5"/></svg></div>
  <div class="icon-disc" style="left:668px;top:322px"><svg width="36" height="36" viewBox="0 0 36 36" fill="none" stroke="#fff" stroke-width="2.4"><path d="M4 32h28M9 32V20M16 32V14M23 32V18M30 32V10M6 14l9-7 7 5 10-8"/></svg></div>
  <div class="col" style="left:176px;top:431px"><h3>OUR MISSION</h3><p>Our core mission is to provide high-quality technical services and practical solutions to solve present-day and future challenges in dynamic permafrost environments vulnerable to climate change.</p></div>
  <div class="col" style="left:543px;top:431px"><h3>OUR VISION</h3><p>We strive to be the clients' trusted advisor of choice by establishing relationships, sharing knowledge, and working to provide innovative solutions.</p></div>
</section>

<section class="slide slide--content" style="top:2075px">
  <svg class="head" viewBox="0 0 700 90" aria-hidden="true"><polygon points="0,0 690,0 645,82 0,82" fill="var(--navy)"/><polygon points="0,82 645,82 643,88 0,88" fill="var(--blue)"/><polygon points="654,82 698,0 700,0 657,86" fill="var(--blue)"/></svg>
  <div class="head__title">OUR SERVICES</div>
  <div class="brand brand--dark"><span class="brand__name">TALIK</span><span class="brand__sub">PERMAFROST CONSULTING</span></div>
  <article class="card" style="left:74px"><div class="card__img" style="background:linear-gradient(180deg,#c9d2d8,#4d5a4c)" role="img" aria-label="Drill rig in a boreal forest with a field worker"></div><h3>PERMAFROST AND GROUND<br>ICE CHARACTERIZATION</h3><div class="card__rule"></div><p>We provide the experience and technical skills needed to successfully and cost-effectively complete geotechnical investigations focused</p></article>
  <article class="card" style="left:387px"><div class="card__img" style="background:linear-gradient(135deg,#c9a348,#e4d53a 50%,#6b6a55)" role="img" aria-label="Coiled ground temperature cables and data loggers"></div><h3>GROUND THERMAL ANALYSIS<br>AND MONITORING</h3><div class="card__rule"></div><p>Ground thermal analysis is reliant on adequate ground temperature measurements. We use state of the art ground temperature cables</p></article>
  <article class="card" style="left:700px"><div class="card__img" style="background:linear-gradient(160deg,#8d98a2,#b8c1c7 55%,#7b8790)" role="img" aria-label="Aerial view of a road crossing tundra"></div><h3>INFRASTRUCTURE PERFORMANCE<br>MONITORING</h3><div class="card__rule"></div><p>We use the latest technology to monitor performance of infrastructure constructed on ice-rich permafrost soils. Our approach has been proven to reduce risk</p></article>
</section>

<section class="slide slide--content" style="top:2733px">
  <svg class="head" viewBox="0 0 700 90" aria-hidden="true"><polygon points="0,0 690,0 645,82 0,82" fill="var(--navy)"/><polygon points="0,82 645,82 643,88 0,88" fill="var(--blue)"/><polygon points="654,82 698,0 700,0 657,86" fill="var(--blue)"/></svg>
  <div class="head__title">RECENT PROJECTS</div>
  <div class="brand brand--dark"><span class="brand__name">TALIK</span><span class="brand__sub">PERMAFROST CONSULTING</span></div>
  <article class="project" style="left:61px"><div class="project__img" style="background:linear-gradient(180deg,#c4c9cd,#6c7176)" role="img" aria-label="Drill rig on snowy rocky ground"></div><div class="project__cap">Copper Ridge Mine, Alaska -<br>Arcline Resources</div></article>
  <article class="project" style="left:378px"><div class="project__img" style="background:linear-gradient(180deg,#8b9072,#2f3128)" role="img" aria-label="Permafrost tunnel with exposed ground ice"></div><div class="project__cap">Birch Creek Project, Alaska - Ridgeway Gold Corporation</div></article>
  <article class="project" style="left:695px"><div class="project__img" style="background:linear-gradient(180deg,#dfe6ec,#8f9aa3)" role="img" aria-label="Aerial view of a coastal gravel road in snow"></div><div class="project__cap">Hudson Coast Fiber Link, Nunavut Territory, Canada, Qamutik Corporation</div></article>
</section>

<section class="slide slide--content" style="top:3391px">
  <svg class="head" viewBox="0 0 700 90" aria-hidden="true"><polygon points="0,0 690,0 645,82 0,82" fill="var(--navy)"/><polygon points="0,82 645,82 643,88 0,88" fill="var(--blue)"/><polygon points="654,82 698,0 700,0 657,86" fill="var(--blue)"/></svg>
  <div class="head__title">RECENT PROJECTS</div>
  <div class="brand brand--dark"><span class="brand__name">TALIK</span><span class="brand__sub">PERMAFROST CONSULTING</span></div>
  <article class="project" style="left:61px"><div class="project__img" style="background:linear-gradient(135deg,#e6e6e6,#9c9c9c)" role="img" aria-label="Grey shaded relief terrain model"></div><div class="project__cap">Bonanza Ridge Project, Yukon Territory, Caribou Mining Corporation</div></article>
  <article class="project" style="left:378px"><div class="project__img" style="background:linear-gradient(135deg,#5a7bd8,#4ab0e0 50%,#3a5ec8)" role="img" aria-label="Blue thermal model map"></div><div class="project__cap">Tanana Hills Project, Alaska - Ptarmigan Mines Ltd</div></article>
  <article class="project" style="left:695px"><div class="project__img" style="background:linear-gradient(180deg,#a9b0a0,#4c4a3e)" role="img" aria-label="Eroding permafrost slope in a mine area"></div><div class="project__cap">Klondike Mine, Yukon Territory, Canada, Stewart Metals</div></article>
</section>

<section class="slide" style="top:4049px">
  <svg class="bg-svg" viewBox="0 0 1048 589" aria-hidden="true">
    <rect width="1048" height="589" fill="var(--navy)"/>
    <polygon points="372,0 384,0 633,589 621,589" fill="#fff"/>
  </svg>
  <svg class="bg-svg" viewBox="0 0 1048 589" role="img" aria-label="Two engineers in hard hats on site, black and white">
    <defs><linearGradient id="site" x1="0" y1="0" x2="1" y2="1"><stop offset="0" stop-color="#d4d6d8"/><stop offset=".5" stop-color="#8e9296"/><stop offset="1" stop-color="#3e4246"/></linearGradient></defs>
    <polygon points="384,0 1048,0 1048,589 633,589" fill="url(#site)"/>
    <polygon points="392,589 632,589 478,332" fill="var(--blue)"/>
  </svg>
  <div class="brand brand--light" style="left:60px;top:40px"><span class="brand__name">TALIK</span><span class="brand__sub">PERMAFROST CONSULTING</span></div>
  <div class="thanks">
    <h1>THANK YOU</h1>
    <ul class="contact">
      <li><svg viewBox="0 0 30 30" fill="#fff"><path d="M8 3l5 6-3 3c1 3 4 6 7 7l3-3 6 5-3 5C13 26 4 17 3 6z"/></svg>(907) 555-0148</li>
      <li><svg viewBox="0 0 30 30" fill="none" stroke="#fff" stroke-width="2"><circle cx="15" cy="15" r="12"/><ellipse cx="15" cy="15" rx="5" ry="12"/><path d="M3 15h24M5 9h20M5 21h20"/></svg>https://talikpermafrost.com/</li>
      <li><svg viewBox="0 0 30 30" fill="none" stroke="#fff" stroke-width="2"><rect x="3" y="7" width="24" height="16"/><path d="M3 7l12 9 12-9"/></svg>dmorgan@talikpermafrost.com</li>
      <li><svg viewBox="0 0 30 30" fill="#fff"><path d="M15 2a8 8 0 0 0-8 8c0 6 8 14 8 14s8-8 8-14a8 8 0 0 0-8-8zm0 11a3 3 0 1 1 0-6 3 3 0 0 1 0 6z"/><ellipse cx="15" cy="26" rx="8" ry="2"/></svg>North America</li>
    </ul>
  </div>
</section>

</body>
</html>
```